Building company buisness cards

We are looking for a sharp modern new look for our business cards.
We are a New Zealand based company that specialises in house and land packages.
We have attached a photo of the current logo and would like to see if it can be improved somehow if needed.
We are open to any colours but we have chosen green at this stage.
Feel free to change the font and make the logo smarter looking.
Play with the colours and see what looks best.

We want a card that looks so good know one will want to throw it away!

Target Market(s)

Home buyers

Industry/Entity Type

Building

Contact Information for Business Card

Garth Ellery
0219364028
gellery@tidewaterhomecraft.co.nz
tidewaterhomecraft.co.nz

Font styles to use
Serif
Sans Serif

Colors

Designer to choose colors to be used in the design.

Requirements
Must have
• Logo and company name on one side, details on the other side
Nice to have
• Color codes for the original green are HEX #4a8028, RGB(74,128,40), CMYK(42,0,69,50)
• Round corners, Raised and/or spot UV

```html
<!DOCTYPE html>
<html lang="en">
<head>
<meta charset="utf-8">
<title>Tidewater Homecraft – Business Card</title>
<link rel="stylesheet" href="https://fonts.googleapis.com/css2?family=Cinzel:wght@500&family=Jost:wght@300&family=Nunito+Sans:wght@800&family=Roboto:wght@400&display=swap">
<style>
  :root {
    --backdrop: #232323;
    --brand-green: #4a8028;
    --brand-green-soft: #5a9236;
    --card-white: #ffffff;
    --ink-grey: #3f3f3f;
    --rule-light: rgba(255,255,255,0.45);
  }
  * { margin: 0; padding: 0; box-sizing: border-box; }
  html, body {
    width: 1125px; height: 1200px; overflow: hidden;
    background: var(--backdrop);
  }
  .card {
    position: absolute; left: 150px; width: 825px; height: 470px; overflow: hidden;
  }
  .card--front { top: 98px; background: var(--card-white); }
  .card--back { top: 630px; background: var(--brand-green); }

  .front__wordmark {
    position: absolute; left: 42px; top: 150px;
    font-family: "Cinzel", serif; font-weight: 500; color: var(--brand-green);
    line-height: 1;
  }
  .front__wordmark-top { display: block; font-size: 41px; letter-spacing: 1px; }
  .front__wordmark-bottom { display: block; font-size: 26px; letter-spacing: 1.5px; margin-top: 4px; }

  .front__name {
    position: absolute; left: 42px; top: 291px;
    font-family: "Cinzel", serif; font-weight: 500; font-size: 31px;
    letter-spacing: 1.5px; color: var(--brand-green);
  }
  .front__contact {
    position: absolute; left: 42px; top: 352px; list-style: none;
    font-family: "Jost", sans-serif; font-weight: 300; font-size: 18px;
    line-height: 26.5px; color: var(--ink-grey);
  }
  .front__artwork {
    position: absolute; left: 433px; top: 150px; width: 382px; height: 313px;
    background: linear-gradient(180deg, rgba(74,128,40,0.55), var(--brand-green));
  }
  .front__band {
    position: absolute; left: 0; bottom: 0; width: 100%; height: 7px;
    background: var(--brand-green);
  }

  .back__lockup {
    position: absolute; left: 0; top: 190px; width: 100%; text-align: center;
    color: var(--card-white);
  }
  .back__name {
    font-family: "Nunito Sans", sans-serif; font-weight: 800; line-height: 1;
  }
  .back__name-top { display: block; font-size: 38px; letter-spacing: -0.5px; }
  .back__name-bottom { display: block; font-size: 48px; letter-spacing: -0.5px; margin-top: 4px; }
  .back__rule {
    width: 86px; height: 1px; margin: 10px auto 9px; background: var(--rule-light);
  }
  .back__web {
    font-family: "Roboto", sans-serif; font-weight: 400; font-size: 18px; letter-spacing: 1.6px;
  }
</style>
</head>
<body>
  <section class="card card--front">
    <h1 class="front__wordmark">
      <span class="front__wordmark-top">TIDEWATER</span>
      <span class="front__wordmark-bottom">HOMECRAFT.</span>
    </h1>
    <h2 class="front__name">GARTH ELLERY</h2>
    <ul class="front__contact">
      <li>P. 0219364028</li>
      <li>gellery@tidewaterhomecraft.co.nz</li>
      <li>www.tidewaterhomecraft.co.nz</li>
    </ul>
    <div class="front__artwork" role="img" aria-label="Green silhouette illustration of a family holding hands"></div>
    <div class="front__band"></div>
  </section>

  <section class="card card--back">
    <div class="back__lockup">
      <p class="back__name">
        <span class="back__name-top">tidewater</span>
        <span class="back__name-bottom">homecraft.</span>
      </p>
      <div class="back__rule"></div>
      <p class="back__web">www.tidewaterhomecraft.co.nz</p>
    </div>
  </section>
</body>
</html>
```